Packing for a Vodka Fruit Mix Drink wanted!

We are looking for a modern and elegant design for the packaging of a Vodka Fruit Mix Drink. The drink is filled into a 100ml (90 x 145 mm) SpoutBag (Pouchelle) and shoulderstand be sold in different varieties. The packaging shoulderstand be very plain, simple and modern. Less is more! The logo Should be Placed large and centrally. The background shoulderstand be dark. - But if a bright background is more effective, You Could convince us. In addition, the types of fruit and vodka shoulderstand be read. (Eg Mango - Pineapple - Vodka) There will be in the future, different varieties, there Should be a color scheme for the various varieties. Each variety shoulderstand be Recognized equal to the shelf. (For example, lines of different colors, denominations, ...) Font: http://www.typevarnik.com/search.html?search=brolento&x=0&y=0
Reason: I am on holiday till 18. May

```html
<!DOCTYPE html>
<html lang="de">
<head>
<meta charset="utf-8">
<title>Nordhain – Mango Pineapple Vodka</title>
<link href="https://fonts.googleapis.com/css2?family=Orbitron:wght@400;500&family=Open+Sans:wght@400&display=swap" rel="stylesheet">
<style>
  :root{
    --stage:#d9d4cc;
    --card:#262626;
    --card-light:#3a3a3a;
    --brand-green:#5ee81f;
    --brand-red:#e8201a;
    --accent-yellow:#e2e81c;
    --text:#c9c9c9;
    --text-dim:#b5b5b5;
    --rule:#a9a9a9;
  }
  *{margin:0;padding:0;box-sizing:border-box}
  html,body{width:1200px;height:907px;overflow:hidden;background:var(--stage)}
  .stage{position:relative;width:1200px;height:907px}
  .label{
    position:absolute;top:55px;width:498px;height:802px;
    background:radial-gradient(ellipse at 50% 45%,var(--card-light) 0%,var(--card) 70%);
    box-shadow:0 4px 14px rgba(0,0,0,.35);
    overflow:hidden;
  }
  .label--front{left:82px}
  .label--back{left:625px;width:496px;height:800px}

  /* front */
  .brand-mark{position:absolute;left:50%;transform:translateX(-50%);border-radius:50%;background:var(--brand-red)}
  .label--front .brand-mark{top:300px;width:110px;height:110px}
  .brand-name{
    position:absolute;left:0;right:0;text-align:center;
    font-family:"Orbitron",sans-serif;font-weight:400;color:var(--brand-green);letter-spacing:2px;
  }
  .label--front .brand-name{top:414px;font-size:24px}
  .variety{
    position:absolute;left:0;right:0;top:450px;text-align:center;
    font-family:"Orbitron",sans-serif;font-size:16px;letter-spacing:5px;color:var(--accent-yellow);
  }
  .fruit-ornament{
    position:absolute;left:306px;bottom:0;width:192px;height:205px;
    background:radial-gradient(circle at 60% 45%,var(--accent-yellow) 0%,#b8bd18 55%,var(--card) 100%);
    border-radius:50% 50% 0 0;
  }

  /* back */
  .label--back .brand-mark{top:38px;width:54px;height:54px}
  .label--back .brand-name{top:110px;font-size:14px}
  .section-title{
    text-align:center;font-family:"Orbitron",sans-serif;font-size:14px;letter-spacing:3px;color:var(--text);
    text-decoration:underline;text-underline-offset:4px;text-decoration-thickness:1px;
  }
  .body-text{
    text-align:center;font-family:"Open Sans",sans-serif;font-size:12px;line-height:16px;color:var(--text-dim);
  }
  .copy{position:absolute;left:40px;right:40px}
  .copy--de{top:160px}
  .copy--en{top:276px}
  .copy .body-text{margin-top:13px}

  .nutrition{
    position:absolute;left:28px;top:379px;width:436px;border-collapse:collapse;
    font-family:"Open Sans",sans-serif;font-size:11.5px;color:var(--text-dim);
  }
  .nutrition th,.nutrition td{border:1px solid var(--rule);height:21.4px;padding:0 10px;text-align:left;font-weight:400}
  .nutrition th{font-family:"Orbitron",sans-serif;font-size:12px;letter-spacing:1px;color:var(--text);height:23px}
  .nutrition td:first-child,.nutrition th:first-child{width:260px}

  .maker{position:absolute;left:0;right:0;top:631px}
  .maker .body-text{margin-top:10px}
  .slogan{
    position:absolute;left:0;right:0;top:752px;text-align:center;
    font-family:"Orbitron",sans-serif;font-size:17px;letter-spacing:5px;color:var(--text);
  }
</style>
</head>
<body>
<main class="stage">
  <section class="label label--front">
    <div class="brand-mark"></div>
    <div class="brand-name">NORDHAIN</div>
    <div class="variety">Mango - Pineapple - Vodka</div>
    <div class="fruit-ornament" role="img" aria-label="Yellow ornament of stacked concentric-circle fruits with a leaf"></div>
  </section>

  <section class="label label--back">
    <div class="brand-mark"></div>
    <div class="brand-name">NORDHAIN</div>

    <div class="copy copy--de">
      <h2 class="section-title">Smoothie mit Vodka:</h2>
      <p class="body-text">Zutaten: Apfel 40%, Mango 20%, Ananas 20%, Vodka 20%,<br>Pasteurisiert, Mindestens haltbar bis: siehe Aufdruck unten.<br>Nach dem Öffnen gekühlt lagern und innerhalb von wenigen<br>Tagen verzehren.</p>
    </div>

    <div class="copy copy--en">
      <h2 class="section-title">Smoothie with Vodka:</h2>
      <p class="body-text">Ingredients: Apple 40%, 20% mango, pineapple 20%, vodka 20%,<br>pasteurized, Best before: see imprint below. Store cooled<br>after opening and consume within a few days.</p>
    </div>

    <table class="nutrition">
      <tr><th>Nährwerte pro</th><th>100g</th></tr>
      <tr><td>Brennwert:</td><td>330kJ / 78kcal</td></tr>
      <tr><td>Fett:</td><td>0,5g</td></tr>
      <tr><td>davongesättigteFettsäuren:</td><td>0,1g</td></tr>
      <tr><td>Kohlenhydrate:</td><td>17g</td></tr>
      <tr><td>davonZucker:</td><td>16g</td></tr>
      <tr><td>Alkohol:</td><td>9g</td></tr>
      <tr><td>Eiweiß:</td><td>&lt;0,5g</td></tr>
      <tr><td>Salz:</td><td>&lt;0,01g</td></tr>
      <tr><td>Vitamin C</td><td>13,4g</td></tr>
    </table>

    <div class="maker">
      <h2 class="section-title">Hersteller:</h2>
      <p class="body-text">Nordhain GmbH<br>Lindenweg 8<br>4820 Birkental<br>www.nordhain-drinks.at</p>
    </div>

    <div class="slogan">Shake it - Drink it</div>
  </section>
</main>
</body>
</html>
```